Postcard Design for QWAL-

We need a postcard designed that is similar to our current example with information but has a few changes for the season. It needs to be an oversized postcard that meets KRTB QWAL requirements.

In the section that says complete car care, I'd like to add a blurb that Summer is here! Make sure your Car is ready and your:
AC is cold
Cooling system is functioning properly
Tires and Alighment are vacation ready

Elsewhere on the card, we need to add that we offer a 3 year/36,000 warranty on parts and labor

We also need to add that we have a 5.0 Brivva Review Score and a 4.9 Lantor Vox score

Colors can change as can font as long as it is easy to read

```html
<!DOCTYPE html>
<html lang="en">
<head>
<meta charset="utf-8">
<title>Copper Gate Auto Repair – Summer Postcard</title>
<link href="https://fonts.googleapis.com/css2?family=Poppins:ital,wght@0,400;0,500;0,600;0,700;0,900;1,700;1,900&family=Oswald:wght@600&family=Allura&display=swap" rel="stylesheet">
<style>
:root{
  --bg:#dcdcdc;
  --white:#ffffff;
  --ink:#111111;
  --green:#8bbb45;
  --green-mid:#78a83a;
  --green-dark:#557a28;
  --green-text:#4f7a22;
  --blue:#5ec4ee;
  --gray-box:#555555;
  --dark-box:#262626;
  --mint:#d7f5e3;
  --star:#f2b01e;
}
*{box-sizing:border-box;margin:0;padding:0}
html,body{width:1200px;height:1200px;overflow:hidden;background:var(--bg);font-family:"Poppins",sans-serif;color:var(--ink)}
.card{position:absolute;left:178px;width:843px;height:469px;background:var(--white);box-shadow:0 4px 10px rgba(0,0,0,.25);overflow:hidden}
.card-front{top:99px}
.card-back{top:625px}
.abs{position:absolute}

/* front */
.brand{left:38px;top:30px;display:flex;align-items:center;gap:8px}
.brand-dot{width:22px;height:22px;border-radius:50%;background:var(--ink)}
.brand-name{font-weight:700;font-size:15px;line-height:17px;color:var(--ink);text-transform:uppercase}
.headline-summer{left:34px;top:100px;font-weight:900;font-style:italic;font-size:69px;line-height:70px;letter-spacing:-1px}
.headline-is{left:36px;top:160px;font-family:"Allura",cursive;font-size:64px;line-height:70px}
.headline-here{left:95px;top:160px;font-weight:900;font-style:italic;font-size:69px;line-height:70px;color:var(--green);letter-spacing:-1px}
.speed-stripes{left:296px;top:172px}
.tagline{left:36px;top:233px;font-weight:900;font-style:italic;font-size:16.5px}
.photo{left:0;top:0}
.check-band{left:0;top:290px}
.check{width:40px;height:40px;border-radius:50%;background:var(--ink);border:3px solid var(--white);display:flex;align-items:center;justify-content:center;top:269px}
.check-label{top:320px;text-align:center;color:var(--white);font-weight:600;font-size:10.5px;line-height:12.5px}
.badge-front{left:360px;top:22px}
.call-label{left:32px;top:380px;font-weight:700;font-size:21px;color:var(--green-text)}
.phone-front{left:32px;top:407px;font-size:22px;font-weight:500;display:flex;align-items:center;gap:6px}
.info-line{left:236px;font-size:16.5px;font-weight:500;display:flex;align-items:center;gap:6px}
.info-line b{font-weight:700}
.divider{left:633px;top:385px;height:48px;border-left:1px dashed #777}
.perks{left:648px;top:383px;font-weight:600;font-size:14.5px;line-height:18.5px;text-transform:uppercase}
.perks .lead{color:var(--green-text)}

/* back */
.back-green{left:0;top:0;width:843px;height:259px;background:var(--green-mid)}
.back-green-left{left:0;top:0;width:472px;height:259px;background:var(--green)}
.script-complete{left:34px;top:30px;font-family:"Allura",cursive;font-size:52px;line-height:60px}
.title-carcare{left:34px;top:76px;font-weight:900;font-style:italic;font-size:57px;line-height:60px;letter-spacing:-1.5px}
.title-carcare span{color:var(--white)}
.ribbon{left:36px;top:140px}
.ribbon-text{left:48px;top:148px;color:var(--white);font-weight:700;font-style:italic;font-size:12.5px}
.intro{left:36px;top:183px;width:340px;font-size:12.6px;line-height:15px}
.badge-back{left:376px;top:36px}
.map{left:594px;top:20px;width:212px;height:174px;border-radius:8px;border:3px solid var(--green-dark);background:linear-gradient(160deg,#dff8e8,var(--mint));overflow:hidden}
.map-address{left:594px;top:207px;display:flex;gap:14px;color:var(--white);font-size:11.5px;line-height:13px}
.feature{top:259px;height:79px;color:var(--white);font-weight:700;font-size:14.5px;line-height:17.5px;display:flex;gap:10px}
.feature-1{left:0;width:237px;background:var(--gray-box);padding:14px 0 0 36px}
.feature-2{left:237px;width:215px;background:var(--dark-box);padding:12px 0 0 26px}
.tick{flex:none;margin-top:3px}
.phone-back{left:34px;top:352px;font-size:32px;font-weight:500;display:flex;align-items:center;gap:14px}
.web-back{left:34px;top:391px;font-size:25.5px;display:flex;align-items:center;gap:16px}
.web-back b{font-weight:700}
.postage{left:506px;top:276px;width:81px;height:64px;border:1px solid #999;font-family:Arial,sans-serif;font-size:7.6px;line-height:10px;text-align:center;padding-top:7px}
.mail-address{left:506px;top:351px;width:262px;height:42px;border:1px solid #999;font-size:12.5px;line-height:15.5px;padding:4px 0 0 10px}
.review-scores{left:506px;top:408px;display:flex;gap:22px}
.score{display:flex;align-items:center;gap:6px}
.score-value{font-weight:700;font-size:20px;color:var(--green-text);line-height:22px}
.score-text{font-size:9.5px;line-height:11px;font-weight:500}
.score-stars{display:block;margin-bottom:2px}
</style>
</head>
<body>

<section class="card card-front">
  <svg class="abs photo" width="843" height="469" viewBox="0 0 843 469" role="img" aria-label="Mechanic in overalls inspecting a silver SUV with its hood open in a repair garage">
    <defs>
      <linearGradient id="garageTone" x1="0" y1="0" x2="1" y2="1">
        <stop offset="0" stop-color="#3a3d42"/>
        <stop offset=".55" stop-color="#6b6f75"/>
        <stop offset="1" stop-color="#2a2c30"/>
      </linearGradient>
    </defs>
    <path d="M475 0 L843 0 L843 360 L510 360 C470 360 420 300 405 230 C398 175 430 60 475 0 Z" fill="url(#garageTone)"/>
  </svg>

  <div class="abs brand">
    <div class="brand-dot"></div>
    <div class="brand-name">Copper Gate<br>Auto Repair</div>
  </div>

  <div class="abs headline-summer">SUMMER</div>
  <div class="abs headline-is">is</div>
  <div class="abs headline-here">HERE</div>
  <svg class="abs speed-stripes" width="58" height="52" viewBox="0 0 58 52">
    <polygon points="10,0 17,0 7,52 0,52" fill="#8bbb45"/>
    <polygon points="23,0 30,0 20,52 13,52" fill="#111"/>
    <polygon points="36,0 43,0 33,52 26,52" fill="#8bbb45"/>
    <polygon points="49,0 56,0 46,52 39,52" fill="#111"/>
  </svg>
  <div class="abs tagline">MAKE SURE YOUR CAR IS READY AND YOUR</div>

  <svg class="abs check-band" width="520" height="70" viewBox="0 0 520 70">
    <path d="M0 0 H143 V70 H0 Z" fill="#8bbb45"/>
    <path d="M143 0 H297 V70 H143 Z" fill="#557a28"/>
    <path d="M297 0 H455 C480 0 490 10 505 30 L532 70 H297 Z" fill="#8bbb45"/>
  </svg>
  <div class="abs check" style="left:61px"><svg width="16" height="16" viewBox="0 0 16 16"><circle cx="8" cy="8" r="8" fill="#fff"/><path d="M4.5 8.2 L7 10.6 L11.5 5.6" stroke="#111" stroke-width="1.8" fill="none"/></svg></div>
  <div class="abs check" style="left:199px"><svg width="16" height="16" viewBox="0 0 16 16"><circle cx="8" cy="8" r="8" fill="#fff"/><path d="M4.5 8.2 L7 10.6 L11.5 5.6" stroke="#111" stroke-width="1.8" fill="none"/></svg></div>
  <div class="abs check" style="left:354px"><svg width="16" height="16" viewBox="0 0 16 16"><circle cx="8" cy="8" r="8" fill="#fff"/><path d="M4.5 8.2 L7 10.6 L11.5 5.6" stroke="#111" stroke-width="1.8" fill="none"/></svg></div>
  <div class="abs check-label" style="left:6px;top:322px;width:150px">AC is cold</div>
  <div class="abs check-label" style="left:149px;width:140px">Cooling system is functioning properly</div>
  <div class="abs check-label" style="left:309px;width:130px">Tires and Alighment are vacation ready</div>

  <svg class="abs badge-front" width="130" height="130" viewBox="0 0 200 200">
    <defs><clipPath id="badgeLowerFront"><rect x="0" y="140" width="200" height="60"/></clipPath></defs>
    <polygon points="200,100 183.1,122.3 186.6,150 160.8,160.8 150,186.6 122.3,183.1 100,200 77.7,183.1 50,186.6 39.2,160.8 13.4,150 16.9,122.3 0,100 16.9,77.7 13.4,50 39.2,39.2 50,13.4 77.7,16.9 100,0 122.3,16.9 150,13.4 160.8,39.2 186.6,50 183.1,77.7" fill="#5ec4ee" stroke="#fff" stroke-width="3"/>
    <polygon points="200,100 183.1,122.3 186.6,150 160.8,160.8 150,186.6 122.3,183.1 100,200 77.7,183.1 50,186.6 39.2,160.8 13.4,150 16.9,122.3 0,100 16.9,77.7 13.4,50 39.2,39.2 50,13.4 77.7,16.9 100,0 122.3,16.9 150,13.4 160.8,39.2 186.6,50 183.1,77.7" fill="#8bbb45" clip-path="url(#badgeLowerFront)"/>
    <polygon points="200,100 183.1,122.3 186.6,150 160.8,160.8 150,186.6 122.3,183.1 100,200 77.7,183.1 50,186.6 39.2,160.8 13.4,150 16.9,122.3 0,100 16.9,77.7 13.4,50 39.2,39.2 50,13.4 77.7,16.9 100,0 122.3,16.9 150,13.4 160.8,39.2 186.6,50 183.1,77.7" fill="none" stroke="#fff" stroke-width="1.6" stroke-dasharray="4 3" transform="translate(12 12) scale(.88)"/>
    <g font-family="Poppins,sans-serif" text-anchor="middle" fill="#111">
      <text x="100" y="55" font-size="11">We offer a</text>
      <text x="100" y="72" font-size="14" font-weight="700">3 YEAR /</text>
      <text x="100" y="122" font-family="Oswald,sans-serif" font-weight="600" font-size="50">36,000</text>
      <text x="100" y="160" font-size="10.5" font-weight="700">Mile warranty on</text>
      <text x="100" y="173" font-size="10.5" font-weight="700">parts and labor</text>
    </g>
  </svg>

  <div class="abs call-label">CALL US NOW</div>
  <div class="abs phone-front">
    <svg width="16" height="16" viewBox="0 0 24 24"><path d="M6.6 10.8a15 15 0 0 0 6.6 6.6l2.2-2.2c.3-.3.7-.4 1-.2 1.1.4 2.3.6 3.6.6.6 0 1 .4 1 1V20c0 .6-.4 1-1 1A17 17 0 0 1 3 4c0-.6.4-1 1-1h3.5c.6 0 1 .4 1 1 0 1.3.2 2.5.6 3.6.1.3 0 .7-.2 1z" fill="#4f7a22"/></svg>
    555-014-0277
  </div>
  <div class="abs info-line" style="top:380px">
    <svg width="14" height="18" viewBox="0 0 14 18"><path d="M7 0a7 7 0 0 0-7 7c0 5 7 11 7 11s7-6 7-11a7 7 0 0 0-7-7z" fill="#4f7a22"/><circle cx="7" cy="7" r="2.6" fill="#fff"/></svg>
    212 Alder Mill Road, Unit B, Fern Hollow
  </div>
  <div class="abs info-line" style="top:410px">
    <svg width="14" height="14" viewBox="0 0 14 14"><circle cx="7" cy="7" r="6" fill="none" stroke="#4f7a22" stroke-width="1.5"/><path d="M1 7h12M7 1c-3 3-3 9 0 12M7 1c3 3 3 9 0 12" stroke="#4f7a22" stroke-width="1.2" fill="none"/></svg>
    <span>www.<b>CopperGateRepair</b>.com</span>
  </div>
  <div class="abs divider"></div>
  <div class="abs perks"><span class="lead">Free Vehicle</span><br>Pick up, drop off,<br>&amp; loaners</div>
</section>

<section class="card card-back">
  <div class="abs back-green"></div>
  <div class="abs back-green-left"></div>

  <div class="abs script-complete">Complete</div>
  <div class="abs title-carcare">CAR <span>CARE</span></div>
  <svg class="abs ribbon" width="302" height="34" viewBox="0 0 302 34"><polygon points="0,0 302,0 284,34 0,34" fill="#557a28"/></svg>
  <div class="abs ribbon-text">INCLUDING INSPECTIONS AND EMISSIONS</div>
  <p class="abs intro">Don't trust your car to just any automotive repair shop. We have the reliable, experienced technicians to quickly diagnose what's wrong &amp; fix it right the first time-saving you time, headaches &amp; money.</p>

  <svg class="abs badge-back" width="186" height="186" viewBox="0 0 200 200">
    <defs><clipPath id="badgeLowerBack"><rect x="0" y="140" width="200" height="60"/></clipPath></defs>
    <polygon points="200,100 183.1,122.3 186.6,150 160.8,160.8 150,186.6 122.3,183.1 100,200 77.7,183.1 50,186.6 39.2,160.8 13.4,150 16.9,122.3 0,100 16.9,77.7 13.4,50 39.2,39.2 50,13.4 77.7,16.9 100,0 122.3,16.9 150,13.4 160.8,39.2 186.6,50 183.1,77.7" fill="#5ec4ee" stroke="#fff" stroke-width="3"/>
    <polygon points="200,100 183.1,122.3 186.6,150 160.8,160.8 150,186.6 122.3,183.1 100,200 77.7,183.1 50,186.6 39.2,160.8 13.4,150 16.9,122.3 0,100 16.9,77.7 13.4,50 39.2,39.2 50,13.4 77.7,16.9 100,0 122.3,16.9 150,13.4 160.8,39.2 186.6,50 183.1,77.7" fill="#8bbb45" clip-path="url(#badgeLowerBack)"/>
    <polygon points="200,100 183.1,122.3 186.6,150 160.8,160.8 150,186.6 122.3,183.1 100,200 77.7,183.1 50,186.6 39.2,160.8 13.4,150 16.9,122.3 0,100 16.9,77.7 13.4,50 39.2,39.2 50,13.4 77.7,16.9 100,0 122.3,16.9 150,13.4 160.8,39.2 186.6,50 183.1,77.7" fill="none" stroke="#fff" stroke-width="1.6" stroke-dasharray="4 3" transform="translate(12 12) scale(.88)"/>
    <g font-family="Poppins,sans-serif" text-anchor="middle" fill="#111">
      <text x="100" y="55" font-size="11">We offer a</text>
      <text x="100" y="72" font-size="14" font-weight="700">3 YEAR /</text>
      <text x="100" y="122" font-family="Oswald,sans-serif" font-weight="600" font-size="50">36,000</text>
      <text x="100" y="160" font-size="10.5" font-weight="700">Mile warranty on</text>
      <text x="100" y="173" font-size="10.5" font-weight="700">parts and labor</text>
    </g>
  </svg>

  <div class="abs map" role="img" aria-label="Street map showing the shop location on Alder Mill Road"></div>
  <div class="abs map-address">
    <svg width="14" height="18" viewBox="0 0 14 18" style="flex:none;margin-left:2px"><path d="M7 0a7 7 0 0 0-7 7c0 5 7 11 7 11s7-6 7-11a7 7 0 0 0-7-7z" fill="#fff"/><circle cx="7" cy="7" r="2.6" fill="#78a83a"/></svg>
    <span>Copper Gate Repair 212<br>Alder Mill Road, Unit B Fern<br>Hollow, PA 17000</span>
  </div>

  <div class="abs feature feature-1">
    <svg class="tick" width="11" height="11" viewBox="0 0 16 16"><circle cx="8" cy="8" r="8" fill="#8bbb45"/><path d="M4.5 8.2 L7 10.6 L11.5 5.6" stroke="#fff" stroke-width="2" fill="none"/></svg>
    <span>Trust in a timely,<br>full-service repair<br>facility.</span>
  </div>
  <div class="abs feature feature-2">
    <svg class="tick" width="11" height="11" viewBox="0 0 16 16"><circle cx="8" cy="8" r="8" fill="#8bbb45"/><path d="M4.5 8.2 L7 10.6 L11.5 5.6" stroke="#fff" stroke-width="2" fill="none"/></svg>
    <span>Enjoy<br>unparalleled<br>customer service</span>
  </div>

  <div class="abs phone-back">
    <svg width="20" height="20" viewBox="0 0 24 24"><path d="M6.6 10.8a15 15 0 0 0 6.6 6.6l2.2-2.2c.3-.3.7-.4 1-.2 1.1.4 2.3.6 3.6.6.6 0 1 .4 1 1V20c0 .6-.4 1-1 1A17 17 0 0 1 3 4c0-.6.4-1 1-1h3.5c.6 0 1 .4 1 1 0 1.3.2 2.5.6 3.6.1.3 0 .7-.2 1z" fill="#4f7a22"/></svg>
    555-014-0277
  </div>
  <div class="abs web-back">
    <svg width="17" height="17" viewBox="0 0 14 14"><circle cx="7" cy="7" r="6" fill="none" stroke="#4f7a22" stroke-width="1.5"/><path d="M1 7h12M7 1c-3 3-3 9 0 12M7 1c3 3 3 9 0 12" stroke="#4f7a22" stroke-width="1.2" fill="none"/></svg>
    <span>www.<b>CopperGateRepair</b>.com</span>
  </div>

  <div class="abs postage">Presorted<br>First-Class Mail<br>U.S. Postage Paid<br>40218</div>
  <div class="abs mail-address">****************ECRWSS****QWAL<br>Local Postal Customer.</div>

  <div class="abs review-scores">
    <div class="score">
      <span class="score-value">5.0</span>
      <span class="score-text">
        <svg class="score-stars" width="60" height="11" viewBox="0 0 60 11"><g fill="#f2b01e"><path id="st" d="M5.5 0l1.6 3.5 3.9.4-2.9 2.6.8 3.8-3.4-2-3.4 2 .8-3.8L0 3.9l3.9-.4z"/><use href="#st" x="12"/><use href="#st" x="24"/><use href="#st" x="36"/><use href="#st" x="48"/></g></svg>
        Brivva Review Score
      </span>
    </div>
    <div class="score">
      <span class="score-value">4.9</span>
      <span class="score-text">
        <svg class="score-stars" width="60" height="11" viewBox="0 0 60 11"><g fill="#f2b01e"><use href="#st"/><use href="#st" x="12"/><use href="#st" x="24"/><use href="#st" x="36"/><use href="#st" x="48"/></g></svg>
        Lantor Vox Score
      </span>
    </div>
  </div>
</section>

</body>
</html>
```